Sports Field sign

Our business provides audio visual solutions to corporate and government clients. We have purchased space at a sports field to place two signs to promote our business. We need to provide the artwork in high res format for a sign to be placed at a sports oval. The physical sign will be 900mm high and 7000mm long. It needs to include our logo, contact number, and the services we offer. It needs to be tidy, easy to read and easily visible from a distance. The sample I have done is very basic but covers what we need - I would expect that a designer can produce an eye-catching impressive sign with this much space to work with., and may even include some flashy background, an image or creative design to get attention.

examples of what signs are up at the oval now here - https://twitter.com/KPQ/status/1742906318845210937?s=20&t=9-bHRm4kwqZuLEO7_f_NxZ

Our Company web site is www.brightlinkav.com.au

```html
<!DOCTYPE html>
<html lang="en">
<head>
<meta charset="utf-8">
<title>Brightlink AV – Sports Field Sign</title>
<link rel="stylesheet" href="https://fonts.googleapis.com/css2?family=Kumbh+Sans:wght@600;800&family=Source+Sans+3:wght@400;600&display=swap">
<style>
  :root {
    --page-grey: #b3b3b3;
    --sign-white: #ffffff;
    --brand-orange: #e85d12;
    --brand-blue: #2b56a8;
    --brand-blue-light: #74b3e6;
    --panel-blue-deep: #1a2f9a;
    --panel-blue: #2550b0;
    --ink: #1c1c1c;
    --divider: rgba(255,255,255,0.75);
  }
  * { box-sizing: border-box; margin: 0; padding: 0; }
  html, body {
    width: 1200px; height: 900px; overflow: hidden;
    background: var(--page-grey);
  }
  .sign {
    position: absolute; left: 77px; top: 380px;
    width: 1069px; height: 137px;
    background: var(--sign-white);
    box-shadow: 0 2px 6px rgba(0,0,0,0.3);
    overflow: hidden;
  }
  .sign-shapes { position: absolute; inset: 0; }
  .brand-square {
    position: absolute; left: 60px; top: 33px;
    width: 60px; height: 60px; background: var(--brand-blue);
  }
  .brand-name {
    position: absolute; left: 186px; top: 37px;
    font-family: "Source Sans 3", sans-serif; font-weight: 400;
    font-size: 26px; line-height: 1; color: var(--ink);
  }
  .brand-rule {
    position: absolute; left: 186px; top: 69px;
    width: 193px; height: 2px; background: var(--brand-orange);
  }
  .tagline {
    position: absolute; left: 186px; top: 75px;
    font-family: "Source Sans 3", sans-serif; font-weight: 400;
    font-size: 9.5px; letter-spacing: 0.1px; color: var(--ink);
  }
  .web-button {
    position: absolute; left: 206px; top: 99px;
    width: 147px; height: 22px; background: var(--brand-orange);
    color: var(--sign-white); font-family: "Source Sans 3", sans-serif;
    font-size: 11px; line-height: 22px; text-align: center;
  }
  .headline {
    position: absolute; left: 585px; top: 22px;
    font-family: "Kumbh Sans", sans-serif; white-space: nowrap;
    color: var(--sign-white); font-weight: 600; font-size: 23px;
  }
  .headline-accent {
    margin-left: 4px;
    color: var(--brand-orange); font-weight: 800; font-size: 32px;
  }
  .services {
    position: absolute; left: 574px; top: 73px;
    display: flex; list-style: none;
    font-family: "Source Sans 3", sans-serif; font-size: 14.5px;
    color: var(--sign-white);
  }
  .service-group {
    padding: 0 10px 0 9px; border-left: 1px solid var(--divider);
    line-height: 18px;
  }
  .service-group:first-child { border-left: none; width: 99px; padding-left: 5px; }
  .service-group:nth-child(2) { width: 110px; }
  .service-group:nth-child(3) { width: 118px; }
  .service-item::before {
    content: ""; display: inline-block; margin-right: 4px;
    border-left: 3px solid transparent; border-right: 3px solid transparent;
    border-bottom: 6px solid var(--brand-orange);
    vertical-align: 4px;
  }
</style>
</head>
<body>
  <section class="sign" aria-label="Brightlink AV sports field sign">
    <svg class="sign-shapes" width="1069" height="137" viewBox="0 0 1069 137">
      <defs>
        <linearGradient id="panel-fill" x1="0" y1="0" x2="1" y2="0">
          <stop offset="0" stop-color="#2a5ab8"/>
          <stop offset="0.5" stop-color="#2449a8"/>
          <stop offset="1" stop-color="#1a2890"/>
        </linearGradient>
        <linearGradient id="band-fill" x1="0" y1="0" x2="0" y2="1">
          <stop offset="0" stop-color="#2b56a8"/>
          <stop offset="0.5" stop-color="#74b3e6"/>
          <stop offset="1" stop-color="#2b56a8"/>
        </linearGradient>
      </defs>
      <polygon class="edge-chevron" points="0,0 6,0 33,68 6,137 0,137" fill="#e85d12"/>
      <rect class="centre-band" role="img" aria-label="Decorative blue graphic band"
            x="430" y="0" width="58" height="137" fill="url(#band-fill)"/>
      <polygon class="divider-chevron" points="495,0 512,0 540,68 512,137 495,137 523,68" fill="#e85d12"/>
      <polygon class="blue-panel" role="img" aria-label="Deep blue panel with flowing wave-line texture"
               points="512,0 1069,0 1069,137 512,137 540,68" fill="url(#panel-fill)"/>
    </svg>

    <div class="brand-square" aria-hidden="true"></div>
    <p class="brand-name">brightlink av</p>
    <div class="brand-rule"></div>
    <p class="tagline">CONNECTING PEOPLE WITH TECHNOLOGY</p>
    <p class="web-button">www.brightlinkav.com.au</p>

    <h1 class="headline">The Experts in <span class="headline-accent">AUDIO VISUAL</span></h1>
    <ul class="services">
      <li class="service-group"><div class="service-item">Hospitality</div><div class="service-item">Recreation</div></li>
      <li class="service-group"><div class="service-item">Orporate</div><div class="service-item">Education</div></li>
      <li class="service-group"><div class="service-item">Medical</div><div class="service-item">Government</div></li>
      <li class="service-group"><div class="service-item">Religious</div><div class="service-item">AV installation</div></li>
    </ul>
  </section>
</body>
</html>
```